Office Stationary and Business Card package

I need a new fresh looking business card and stationary design. "I need to refresh and update my Stationary and Business card appearance.

We are a family dental practice that handles all phases of dentistry including cosmetic, emergency and implant restoration We like the use of Blue and Grey in the design. i would like to include my website address and Phone numbers on the new project as well as a choice of different back sides to business cards which might include a map, appointment information, or blank depending on the particular card. The business cards should allow for the inclusion of another persons name and title in some location.

Information to be included in stationery:

Dorian T Valbeck DMD, FAIDS
A Professional Dental Corporation (this needs to be
somewhere on the stationary and business cards)
48610 Marlow Lane
Alder Grove, CA 94127
PHONE: (562) 317-5092
WEBSITE: www.dorianvalbeckdmd.example

Designs need to be Vibrant, Professional and Clean.
Colors to use: Blue, Grey and White colors.

I currently do not have an existing logo. I would like something simply, similar to the attached.

```html
<!DOCTYPE html>
<html lang="en">
<head>
<meta charset="utf-8">
<title>Valbeck Dental – Stationery Set</title>
<link rel="stylesheet" href="https://fonts.googleapis.com/css2?family=Open+Sans:wght@400;600;700&display=swap">
<style>
  :root {
    --blue: #1b74c2;
    --blue-deep: #155f9f;
    --grey: #4a4b4e;
    --grey-soft: #8a8c90;
    --paper: #ffffff;
    --stage: #e9eaec;
    --ink: #3a3b3e;
  }
  * { box-sizing: border-box; margin: 0; padding: 0; }
  html, body { width: 1200px; height: 3322px; overflow: hidden; }
  body {
    background: var(--stage);
    font-family: "Open Sans", Arial, sans-serif;
    color: var(--ink);
    display: flex;
    flex-direction: column;
    justify-content: space-evenly;
    align-items: center;
  }
  .row { display: flex; gap: 40px; }
  .sheet {
    position: relative;
    background: var(--paper);
    box-shadow: 0 6px 18px rgba(0,0,0,.12);
    overflow: hidden;
  }
  .sheet > svg.shapes { position: absolute; inset: 0; width: 100%; height: 100%; }
  .sheet .content { position: absolute; inset: 0; }

  .brand { display: inline-flex; align-items: center; gap: 8px; color: var(--blue); font-weight: 700; white-space: nowrap; }
  .brand-dot { border-radius: 50%; background: var(--blue); flex: none; }

  .card { width: 500px; height: 286px; }
  .letterhead { width: 500px; height: 707px; }
  .slip { width: 1040px; height: 490px; }
  .envelope { width: 1040px; height: 490px; }

  .contact .name { font-size: 15px; font-weight: 700; color: var(--blue); white-space: nowrap; }
  .contact .name small { font-size: 10px; font-weight: 600; }
  .contact .corp { font-size: 11px; font-weight: 600; color: var(--blue-deep); margin-bottom: 6px; white-space: nowrap; }
  .contact p { font-size: 10.5px; line-height: 1.55; color: var(--grey); white-space: nowrap; }

  /* business card front */
  .card-front .brand { position: absolute; left: 28px; top: 26px; font-size: 16px; }
  .card-front .brand-dot { width: 14px; height: 14px; }
  .card-front .contact { position: absolute; left: 28px; top: 70px; }

  /* business card back */
  .card-back .brand { position: absolute; left: 50%; top: 50%; transform: translate(-50%,-50%); font-size: 24px; }
  .card-back .brand-dot { width: 20px; height: 20px; }

  /* business card alternate front */
  .card-alt .brand { position: absolute; left: 26px; top: 34px; font-size: 15px; }
  .card-alt .brand-dot { width: 13px; height: 13px; }
  .card-alt .contact { position: absolute; left: 200px; top: 30px; }

  /* letterhead */
  .letter .brand { position: absolute; left: 34px; top: 46px; font-size: 14px; }
  .letter .brand-dot { width: 12px; height: 12px; }
  .letter .header-info { position: absolute; right: 30px; top: 42px; text-align: right; }
  .letter .header-info .name { font-size: 10px; font-weight: 700; color: var(--blue); }
  .letter .header-info p { font-size: 7.5px; line-height: 1.5; color: var(--grey); }
  .letter .body { position: absolute; left: 46px; right: 46px; top: 150px; font-size: 8.5px; line-height: 1.6; color: var(--ink); }
  .letter .body p { margin-bottom: 10px; }
  .fees { width: 62%; border-collapse: collapse; margin: 6px 0 14px; font-size: 8px; }
  .fees td { padding: 3px 4px; border-bottom: 1px solid #cfd1d4; }
  .fees td.amount { text-align: right; }
  .fees tr:last-child td { border-bottom: 1.5px solid var(--grey); }

  .letter-back .brand { position: absolute; left: 50%; top: 50%; transform: translate(-50%,-50%); font-size: 34px; }
  .letter-back .brand-dot { width: 28px; height: 28px; }

  /* compliments slip */
  .slip .brand { position: absolute; left: 56px; top: 60px; font-size: 26px; }
  .slip .brand-dot { width: 22px; height: 22px; }
  .slip .contact { position: absolute; left: 56px; top: 130px; }
  .slip .contact .name { font-size: 22px; }
  .slip .contact .name small { font-size: 14px; }
  .slip .contact .corp { font-size: 15px; }
  .slip .contact p { font-size: 14px; }
  .slip .greeting { position: absolute; left: 56px; bottom: 34px; font-size: 22px; font-weight: 600; color: var(--paper); }

  /* envelope */
  .envelope .brand { position: absolute; left: 56px; top: 54px; font-size: 26px; }
  .envelope .brand-dot { width: 22px; height: 22px; }
  .envelope .contact { position: absolute; left: 56px; top: 118px; }
  .envelope .contact .name { font-size: 20px; }
  .envelope .contact .name small { font-size: 13px; }
  .envelope .contact .corp { font-size: 14px; }
  .envelope .contact p { font-size: 13px; }
</style>
</head>
<body>

  <section class="row">
    <article class="sheet card card-front">
      <svg class="shapes" viewBox="0 0 500 286" preserveAspectRatio="none" aria-hidden="true">
        <polygon points="0,0 150,0 0,16" fill="var(--blue)"/>
        <polygon points="0,0 60,0 0,7" fill="var(--grey)"/>
        <polygon points="0,232 500,252 500,286 0,286" fill="var(--blue)"/>
        <polygon points="340,286 500,242 500,286" fill="var(--grey)"/>
      </svg>
      <div class="content">
        <div class="brand"><span class="brand-dot"></span>Valbeck Dental</div>
        <div class="contact">
          <div class="name">Dorian T Valbeck <small>DMD, FAIDS</small></div>
          <div class="corp">A Professional Dental Corporation</div>
          <p>48610 Marlow Lane, Alder Grove, CA 94127</p>
          <p>(562) 317-5092</p>
          <p>www.dorianvalbeckdmd.example</p>
        </div>
      </div>
    </article>

    <article class="sheet card card-back">
      <svg class="shapes" viewBox="0 0 500 286" preserveAspectRatio="none" aria-hidden="true">
        <polygon points="250,0 500,0 500,74" fill="var(--blue)"/>
        <polygon points="430,0 500,0 500,20" fill="var(--grey)"/>
        <polygon points="0,218 330,286 0,286" fill="var(--blue)"/>
        <polygon points="360,286 500,236 500,286" fill="var(--grey)"/>
      </svg>
      <div class="content">
        <div class="brand"><span class="brand-dot"></span>Valbeck Dental</div>
      </div>
    </article>
  </section>

  <section class="row">
    <article class="sheet letterhead letter">
      <svg class="shapes" viewBox="0 0 500 707" preserveAspectRatio="none" aria-hidden="true">
        <polygon points="0,0 500,0 500,6 0,28" fill="var(--blue)"/>
        <polygon points="0,0 120,0 0,12" fill="var(--grey)"/>
        <polygon points="0,648 500,672 500,707 0,707" fill="var(--blue)"/>
        <polygon points="370,707 500,660 500,707" fill="var(--grey)"/>
      </svg>
      <div class="content">
        <div class="brand"><span class="brand-dot"></span>Valbeck Dental</div>
        <div class="header-info">
          <div class="name">Dorian T Valbeck DMD, FAIDS</div>
          <p>A Professional Dental Corporation</p>
          <p>48610 Marlow Lane, Alder Grove, CA 94127</p>
          <p>(562) 317-5092 · www.dorianvalbeckdmd.example</p>
        </div>
        <div class="body">
          <p>Dear patient, thank you for choosing our practice for your family dental care. We are glad to welcome you and look forward to helping you keep a healthy, bright smile for years to come.</p>
          <p>Below is a summary of the treatment discussed at your last visit. Please contact our office with any questions about your plan or your insurance coverage.</p>
          <table class="fees">
            <tr><td>Routine exam</td><td class="amount">$85.00</td></tr>
            <tr><td>Cleaning</td><td class="amount">$120.00</td></tr>
            <tr><td>Digital x-rays</td><td class="amount">$95.00</td></tr>
            <tr><td>Composite filling</td><td class="amount">$180.00</td></tr>
            <tr><td>Whitening tray</td><td class="amount">$250.00</td></tr>
          </table>
          <p>We look forward to seeing you soon.</p>
          <p>Sincerely,</p>
        </div>
      </div>
    </article>

    <article class="sheet letterhead letter-back">
      <svg class="shapes" viewBox="0 0 500 707" preserveAspectRatio="none" aria-hidden="true">
        <polygon points="170,0 500,0 500,64" fill="var(--blue)"/>
        <polygon points="420,0 500,0 500,18" fill="var(--grey)"/>
        <polygon points="0,610 380,707 0,707" fill="var(--blue)"/>
        <polygon points="330,707 500,632 500,707" fill="var(--grey)"/>
      </svg>
      <div class="content">
        <div class="brand"><span class="brand-dot"></span>Valbeck Dental</div>
      </div>
    </article>
  </section>

  <article class="sheet slip">
    <svg class="shapes" viewBox="0 0 1040 490" preserveAspectRatio="none" aria-hidden="true">
      <polygon points="0,0 260,0 0,22" fill="var(--blue)"/>
      <polygon points="0,0 110,0 0,10" fill="var(--grey)"/>
      <polygon points="0,368 1040,410 1040,490 0,490" fill="var(--blue)"/>
      <polygon points="720,490 1040,386 1040,490" fill="var(--grey)"/>
    </svg>
    <div class="content">
      <div class="brand"><span class="brand-dot"></span>Valbeck Dental</div>
      <div class="contact">
        <div class="name">Dorian T Valbeck <small>DMD, FAIDS</small></div>
        <div class="corp">A Professional Dental Corporation</div>
        <p>48610 Marlow Lane, Alder Grove, CA 94127</p>
        <p>(562) 317-5092</p>
        <p>www.dorianvalbeckdmd.example</p>
      </div>
      <div class="greeting">With compliments</div>
    </div>
  </article>

  <article class="sheet envelope">
    <svg class="shapes" viewBox="0 0 1040 490" preserveAspectRatio="none" aria-hidden="true">
      <polygon points="0,0 260,0 0,22" fill="var(--blue)"/>
      <polygon points="0,0 110,0 0,10" fill="var(--grey)"/>
      <polygon points="0,400 1040,430 1040,490 0,490" fill="var(--blue)"/>
      <polygon points="780,490 1040,404 1040,490" fill="var(--grey)"/>
    </svg>
    <div class="content">
      <div class="brand"><span class="brand-dot"></span>Valbeck Dental</div>
      <div class="contact">
        <div class="name">Dorian T Valbeck <small>DMD, FAIDS</small></div>
        <div class="corp">A Professional Dental Corporation</div>
        <p>48610 Marlow Lane</p>
        <p>Alder Grove, CA 94127</p>
      </div>
    </div>
  </article>

  <section class="row">
    <article class="sheet card card-alt">
      <svg class="shapes" viewBox="0 0 500 286" preserveAspectRatio="none" aria-hidden="true">
        <polygon points="0,0 150,0 0,16" fill="var(--blue)"/>
        <polygon points="0,0 60,0 0,7" fill="var(--grey)"/>
        <polygon points="0,226 500,248 500,286 0,286" fill="var(--blue)"/>
        <polygon points="350,286 500,238 500,286" fill="var(--grey)"/>
      </svg>
      <div class="content">
        <div class="brand"><span class="brand-dot"></span>Valbeck Dental</div>
        <div class="contact">
          <div class="name">Dorian T Valbeck <small>DMD, FAIDS</small></div>
          <div class="corp">A Professional Dental Corporation</div>
          <p>48610 Marlow Lane, Alder Grove, CA 94127</p>
          <p>(562) 317-5092</p>
          <p>www.dorianvalbeckdmd.example</p>
        </div>
      </div>
    </article>

    <article class="sheet card card-back">
      <svg class="shapes" viewBox="0 0 500 286" preserveAspectRatio="none" aria-hidden="true">
        <polygon points="0,0 230,0 0,70" fill="var(--blue)"/>
        <polygon points="0,0 70,0 0,20" fill="var(--grey)"/>
        <polygon points="170,286 500,214 500,286" fill="var(--blue)"/>
        <polygon points="400,286 500,256 500,286" fill="var(--grey)"/>
      </svg>
      <div class="content">
        <div class="brand"><span class="brand-dot"></span>Valbeck Dental</div>
      </div>
    </article>
  </section>

</body>
</html>
```